IG ad to attract older men for better health #1

I want a bold headline Instagram Ad that coordinate with my website design with a racy sexy woman to attract men 45yrs old plus. See Two samples attached

Target Market(s)

Men 45 years old and older

Industry/Entity Type

Health And Wellness

Requirements
Must have
• eye catching appeal to men
Nice to have
• The copy to read
Kestrel61go is the headline at the top of the page. Then the copy reads...
"I want to seduce you to better health with a little T&A. Remove the excuses, provide ridiculously simple tips and advice to get you started on a path of lasting heath." Want more?

```html
<!DOCTYPE html>
<html lang="en">
<head>
<meta charset="utf-8">
<title>IG Post Banner – Kestrel61go</title>
<link rel="stylesheet" href="https://fonts.googleapis.com/css2?family=Poppins:wght@300;400&family=Titan+One&family=Oswald:wght@300;400;500&family=Dosis:wght@400;700&display=swap">
<style>
  :root {
    --board: #4b4b4b;
    --board-light: #575757;
    --board-line: #6e6e6e;
    --label: #ffffff;
    --pink: #ee3d8f;
    --pink-panel: rgba(240, 88, 157, 0.9);
    --pink-line: #f06aa6;
    --teal: #14b39c;
    --orange: #f5961e;
    --ink: #1c1c1c;
    --white: #ffffff;
  }
  * { box-sizing: border-box; margin: 0; padding: 0; }
  html, body { width: 1200px; height: 720px; overflow: hidden; }
  body {
    background: radial-gradient(ellipse at center, var(--board-light) 0%, var(--board) 70%);
    font-family: "Poppins", sans-serif;
    position: relative;
  }
  .board-frame {
    position: absolute; inset: 8px;
    border: 1px solid var(--board-line);
  }
  .board-title {
    position: absolute; top: 74px; left: 0; width: 1200px;
    text-align: center; color: var(--label);
    font-weight: 300; font-size: 22px; letter-spacing: 0.3px;
  }
  .banner-label {
    position: absolute; top: 154px; width: 432px;
    text-align: center; color: var(--label);
    font-weight: 300; font-size: 18px;
  }
  .banner {
    position: absolute; top: 196px; width: 432px; height: 432px;
    overflow: hidden;
    box-shadow: 0 6px 24px rgba(0,0,0,0.35);
  }
  .banner--beach { left: 114px; }
  .banner--coast { left: 627px; }
  .banner-label--one { left: 114px; }
  .banner-label--two { left: 627px; }

  .scene { position: absolute; inset: 0; }
  .scene--beach {
    background: linear-gradient(180deg, #2b8fd6 0%, #58bde8 30%, #8fd8ef 52%, #3ec7d2 62%, #9fdfe0 74%, #e9e3cf 86%, #efe6d3 100%);
  }
  .scene--coast {
    background: linear-gradient(180deg, #f4f4f4 0%, #e7e8e9 48%, #c9cdcf 62%, #dadcdc 78%, #9c9a96 100%);
  }
  .model {
    position: absolute;
    background: linear-gradient(180deg, #8f6a55 0%, #b07b5e 35%, #a86f52 70%, #5b3b3a 100%);
    border-radius: 40% 40% 0 0 / 14% 14% 0 0;
  }
  .banner--beach .model { left: 276px; top: 62px; width: 150px; height: 370px; }
  .banner--coast .model { left: 268px; top: 86px; width: 150px; height: 346px; }

  .banner-inset {
    position: absolute; inset: 7px;
    border: 1px solid rgba(255,255,255,0.45);
    pointer-events: none;
  }

  .beach-headline {
    position: absolute; left: 22px; top: 82px; width: 244px;
    font-family: "Titan One", sans-serif; font-size: 38px;
    color: var(--pink); line-height: 1; white-space: nowrap;
  }
  .beach-copy-box {
    position: absolute; left: 28px; top: 138px; width: 232px; height: 234px;
    background: rgba(255,255,255,0.78);
    padding: 28px 8px 0;
    text-align: center;
  }
  .beach-copy {
    font-family: "Oswald", sans-serif; font-weight: 300; font-style: oblique 8deg;
    font-size: 19px; line-height: 24.8px; color: var(--ink);
  }
  .beach-cta {
    font-family: "Oswald", sans-serif; font-weight: 500; font-style: oblique 8deg;
    font-size: 23px; line-height: 26px; color: var(--pink); margin-top: 0;
  }

  .coast-brand {
    position: absolute; left: 46px; top: 38px; width: 236px;
    text-align: center;
  }
  .coast-brand-dot {
    display: block; width: 16px; height: 16px; margin: 0 auto 8px;
    border-radius: 50%; background: var(--orange);
  }
  .coast-brand-name {
    font-family: "Dosis", sans-serif; font-weight: 700;
    font-size: 40px; line-height: 1; color: var(--teal);
  }
  .coast-rule { position: absolute; height: 2px; background: var(--pink-line); }
  .coast-rule--top { left: 24px; top: 126px; width: 197px; }
  .coast-rule--bottom { left: 89px; top: 364px; width: 191px; }
  .coast-copy-box {
    position: absolute; left: 24px; top: 129px; width: 290px; height: 233px;
    background: var(--pink-panel);
    padding: 24px 18px 0;
    text-align: center; color: var(--white);
  }
  .coast-copy {
    font-family: "Dosis", sans-serif; font-weight: 400;
    font-size: 19px; line-height: 26.4px;
  }
  .coast-cta {
    font-family: "Dosis", sans-serif; font-weight: 700;
    font-size: 22px; line-height: 26px;
  }
</style>
</head>
<body>
  <div class="board-frame"></div>
  <h1 class="board-title">IG Post Banner</h1>

  <p class="banner-label banner-label--one">Banner-1</p>
  <p class="banner-label banner-label--two">Banner-2</p>

  <section class="banner banner--beach">
    <div class="scene scene--beach" role="img" aria-label="Tropical beach with palm fronds, turquoise sea and bright sky"></div>
    <div class="model" role="img" aria-label="Fit grey-haired man in swim briefs standing on the beach"></div>
    <h2 class="beach-headline">Kestrel61go</h2>
    <div class="beach-copy-box">
      <p class="beach-copy">I want to seduce you to better health with a little T&amp;A. Remove the excuses, provide ridiculously simple tips and advice to get you started on a path of lasting heath."</p>
      <p class="beach-cta">Want more?</p>
    </div>
    <div class="banner-inset"></div>
  </section>

  <section class="banner banner--coast">
    <div class="scene scene--coast" role="img" aria-label="Misty seashore with a rock rising from the water"></div>
    <div class="model" role="img" aria-label="Fit grey-haired man in swim briefs standing by the sea"></div>
    <div class="coast-brand">
      <span class="coast-brand-dot"></span>
      <h2 class="coast-brand-name">Kestrel61go</h2>
    </div>
    <div class="coast-rule coast-rule--top"></div>
    <div class="coast-copy-box">
      <p class="coast-copy">I want to seduce you to better health with a little T&amp;A. Remove the excuses, provide ridiculously simple tips and advice to get you started on a path of lasting heath."</p>
      <p class="coast-cta">Want more?</p>
    </div>
    <div class="coast-rule coast-rule--bottom"></div>
    <div class="banner-inset"></div>
  </section>
</body>
</html>
```